Luxury Face Oil Label

I'm looking for a simple and sophisticated design for a natural face oil that will target the luxe market. It is a pure Natural product. I have attached the logo, Velumi Organics.

Here's the Copy

LUXE FACIAL OIL

Regenerate. Hydrate. Glow

100% Natural

30ml (1.01 oz)

A complex blend of Pure Oils including Marula, Sea Buckthorn, Rosehip, Neroli, Evening primrose, Argan, Calendula, Lavender, Jojoba, Grapeseed, Baobab, Moringa and Vitamin E oil.

Produced by
Tamsin Ridge Ltd
P.O box 7925-00300
Nairobi, Kenya
www.velumiorganics.example

Target Market(s)

High end

Requirements
Must have
• Simple, Please consider the bottle, which is a 30ml clear glass bottle with a gold and white pump. Image attached.
Nice to have
• Very clean designs, not too much going on.
Should not have
• Leaves and nuts.

```html
<!DOCTYPE html>
<html lang="en">
<head>
<meta charset="utf-8">
<title>Velumi Organics – Luxe Facial Oil Label</title>
<link href="https://fonts.googleapis.com/css2?family=Barlow:wght@300;400;500;600&display=swap" rel="stylesheet">
<style>
  :root {
    --backdrop: #d6d5ce;
    --band: #b8b89b;
    --label-white: #ffffff;
    --accent: #8f9266;
    --ink: #4a4a44;
    --ink-soft: #6b6b63;
    --band-text: #f7f7f0;
  }
  * { margin: 0; padding: 0; box-sizing: border-box; }
  html, body {
    width: 1200px; height: 900px; overflow: hidden;
    background: var(--backdrop);
    font-family: "Barlow", Arial, sans-serif;
    color: var(--ink);
  }
  .label {
    position: absolute; left: 60px; top: 220px;
    width: 1080px; height: 460px;
    display: grid; grid-template-columns: repeat(3, 1fr);
    box-shadow: 0 6px 24px rgba(0,0,0,0.08);
  }
  .panel {
    display: grid; grid-template-rows: 75px 1fr 90px;
    border-right: 1px dashed rgba(0,0,0,0.08);
  }
  .panel:last-child { border-right: none; }
  .band { background: var(--band); }
  .panel-body { background: var(--label-white); padding: 70px 44px 0; }

  .side-heading { color: var(--accent); font-size: 19px; font-weight: 500; margin-bottom: 10px; }
  .side-text { font-size: 14.5px; font-weight: 300; line-height: 1.45; color: var(--ink-soft); }

  .panel-front .panel-body {
    padding: 36px 20px 0; text-align: center;
    display: flex; flex-direction: column; align-items: center;
  }
  .brand { display: flex; align-items: center; gap: 10px; margin-bottom: 22px; }
  .brand-mark { width: 14px; height: 14px; border: 1.5px solid var(--accent); }
  .brand-name {
    font-size: 17px; font-weight: 400; letter-spacing: 0.28em;
    text-transform: uppercase; color: var(--accent);
  }
  .product-name { font-size: 30px; font-weight: 500; letter-spacing: 0.02em; color: var(--ink); margin-top: 34px; }
  .tagline { font-size: 15.5px; font-weight: 400; color: var(--ink-soft); margin-top: 4px; }

  .spec-band {
    background: var(--band); color: var(--band-text);
    display: flex; justify-content: center; align-items: center; gap: 30px;
  }
  .spec { text-align: center; line-height: 1.1; }
  .spec-main { font-size: 22px; font-weight: 600; }
  .spec-sub { font-size: 14px; font-weight: 400; }
  .spec-divider { width: 1px; height: 54px; background: var(--band-text); opacity: 0.8; }
</style>
</head>
<body>
  <div class="label">
    <section class="panel panel-contact">
      <div class="band"></div>
      <div class="panel-body">
        <h2 class="side-heading">Contact</h2>
        <p class="side-text">Produced by<br>Tamsin Ridge Ltd<br>P.O box 7925-00300<br>Nairobi, Kenya<br>www.velumiorganics.example</p>
      </div>
      <div class="band"></div>
    </section>

    <section class="panel panel-front">
      <div class="band"></div>
      <div class="panel-body">
        <div class="brand">
          <span class="brand-mark"></span>
          <span class="brand-name">Velumi Organics</span>
        </div>
        <h1 class="product-name">LUXE FACIAL OIL</h1>
        <p class="tagline">Regenerate. Hydrate. Glow</p>
      </div>
      <div class="spec-band">
        <div class="spec"><div class="spec-main">100%</div><div class="spec-sub">Natural</div></div>
        <div class="spec-divider"></div>
        <div class="spec"><div class="spec-main">30ML</div><div class="spec-sub">(1.01 OZ)</div></div>
      </div>
    </section>

    <section class="panel panel-ingredients">
      <div class="band"></div>
      <div class="panel-body">
        <h2 class="side-heading">Ingredients</h2>
        <p class="side-text">A complex blend of Pure Oils including Marula, Sea Buckthorn, Rosehip, Neroli, Evening primrose, Argan, Calendula, Lavender, Jojoba, Grapeseed, Baobab, Moringa and Vitamin E oil.</p>
      </div>
      <div class="band"></div>
    </section>
  </div>
</body>
</html>
```